依頼詳細
コンセプトは「選べる婚活スタイル」です。
①仲人型婚活、②婚活パーティー運営、の2本柱がウリとなります。
ターゲットは20代後半~30代の女性、30代~40代前半の男性です。

色は下記のサイトを参考に
「色数少なめ」「白ベース」「サブカラーにゴールド」
を使用してください。
https://boutique.fenolu.jp/
http://quillmerdon.com/

▼ロゴは下記からダウンロードしてご利用ください。
http://16.bunkobox.nu/0118-a72cd40b9114ea8731811acf9e62c5b3d7

▼写真は下記からダウンロードしてご利用ください。
http://16.bunkobox.nu/0118-m58146b836c907d628221c7316b52e8c3

・スライドショーの部分に「top_slide.jpg」を利用してください。
・「婚活カウンセラー」の部分に「counselor.jpg」を利用してください。
・その他の写真に関しては特に指定はありません。
・フリーの写真素材で良いものがあれば、ご提案願います。(スライドショーの残り3パターン等)
サイトURL
https://selumia.jp/
ページ数
2ページ
希望イメージ
• +5 0 +5
• シンプル
複雑
• 単色
カラフル
• 暗い
明るい
• 日常
高級
• 遊び心
厳粛
• 未来的
伝統的
• 女性的
男性的
納品ファイル
• 高解像度JPG (.jpg)
• イラストレーター形式 (.ai)
• フォトショップ形式 (.psd)
• PNG形式 (.png)
補足説明
シンプルなデザインのサイトのため、バナー等のデザインクオリティがポイントになってくると思います。
----------
・「SELUMIAは成婚主義の結婚相談所です!」の図
・「SELUMIAの3つの特徴」の図
・「初めての方へ」バナー
・「会員数/実績データ」バナー
・「ご成婚までの流れ」バナー
----------
宜しくお願い致します。
依頼公開後の追記内容
ワイヤーフレームに
スライドショーエリアのキャッチコピーを追加しました。
-----------------------------------------------------
多くの結婚式をプロデュースしてきたルシェバルが
あなたの婚活を完全サポート

わたし達だから知っている ‘成婚の法則’
応募くださったランサーの皆様
素敵なデザインのご提案ありがとうございます。

現在、応募案の選定を検討しておりますが、
選定にしばらく時間がかかりそうなため、
その間も応募を受付させていただきます。

新たなアイデア等、ありましたらご提案いただければ幸いです。
引き続きよろしくお願いいたします。
トップページに表示する具体的なテキスト文章が用意できましたので

```html
<!DOCTYPE html>
<html lang="ja">
<head>
<meta charset="utf-8">
<title>SELUMIA 結婚相談所</title>
<link href="https://fonts.googleapis.com/css2?family=Noto+Serif+JP:wght@400;500;700&family=Noto+Sans+JP:wght@400;500&family=Cormorant+Garamond:ital,wght@0,500;1,500&display=swap" rel="stylesheet">
<style>
:root{
  --gold:#b59a5f;
  --gold-dark:#9a7f45;
  --gold-light:#d9c79c;
  --cream:#f7f2e8;
  --text:#5a5248;
  --muted:#8b8276;
  --line:#e3d8c2;
  --white:#ffffff;
}
*{margin:0;padding:0;box-sizing:border-box}
html,body{width:1200px;height:4872px;overflow:hidden}
body{position:relative;background:var(--white);color:var(--text);font-family:"Noto Sans JP",sans-serif;font-size:13px;line-height:1.9}
.ph{display:block}
a{color:inherit;text-decoration:none}
.en{font-family:"Cormorant Garamond",serif;font-style:italic;color:var(--gold)}

/* header */
.site-header{height:150px;padding:0 60px;border-bottom:1px solid var(--line)}
.header-top{display:flex;justify-content:space-between;align-items:center;height:92px}
.brand{display:flex;align-items:center;gap:16px}
.brand-name{font-family:"Noto Serif JP",serif;font-size:30px;letter-spacing:.12em;color:var(--gold)}
.brand-sub{font-size:11px;color:var(--muted);line-height:1.5}
.contact{text-align:right}
.tel{font-family:"Noto Serif JP",serif;font-size:22px;color:var(--gold-dark);display:flex;align-items:center;justify-content:flex-end;gap:8px;line-height:1.4}
.tel-note{font-size:10px;color:var(--muted)}
.header-btns{display:flex;gap:6px;margin-top:4px}
.btn-s{background:var(--gold);color:var(--white);font-size:11px;padding:3px 16px}
.btn-s.light{background:var(--gold-light)}
.gnav{display:flex;height:56px;align-items:center}
.gnav a{font-family:"Noto Serif JP",serif;font-size:13px;padding:0 30px;border-left:1px solid var(--line);text-align:center;line-height:1.4}
.gnav a:last-child{border-right:1px solid var(--line)}
.gnav small{display:block;font-family:"Cormorant Garamond",serif;font-style:italic;color:var(--gold);font-size:11px}

/* hero */
.hero{position:relative;height:380px}
.hero .ph{width:100%;height:100%;background:linear-gradient(180deg,#f3efe9 0%,#e6ddd2 55%,#3e3a3a 56%,#2c2a2c 100%)}
.hero-copy{position:absolute;left:0;right:0;top:150px;text-align:center}
.hero-copy h1{display:inline-block;font-family:"Noto Serif JP",serif;font-weight:700;font-size:34px;line-height:1.5;color:var(--white);background:rgba(60,50,40,.55);padding:4px 28px;letter-spacing:.06em}
.hero-copy p{display:inline-block;margin-top:10px;font-family:"Noto Serif JP",serif;font-size:15px;color:var(--white);background:rgba(60,50,40,.55);padding:2px 22px}
.dots{display:flex;justify-content:center;gap:10px;height:40px;align-items:center}
.dots span{width:9px;height:9px;border-radius:50%;background:var(--line)}
.dots span:first-child{background:var(--gold)}

/* section heads */
.sec-head{text-align:center}
.sec-head .en{font-size:26px;display:block;line-height:1.3}
.sec-head .ja{font-family:"Noto Serif JP",serif;font-size:12px;color:var(--muted)}
.rule{display:flex;align-items:center;justify-content:center;gap:14px;color:var(--gold);font-family:"Noto Serif JP",serif;font-size:18px;letter-spacing:.15em}
.rule:before,.rule:after{content:"";width:90px;height:1px;background:var(--gold-light)}

/* features */
.features{position:relative;height:400px;padding-top:30px;background:linear-gradient(180deg,#fff 0%,#fbf8f2 100%)}
.features .ph{position:absolute;left:0;top:20px;width:520px;height:370px;background:linear-gradient(90deg,#ddd6cf 0%,#eeeae5 60%,rgba(251,248,242,0) 100%)}
.features-text{position:relative;width:760px;margin:10px 0 0 340px;text-align:center;font-family:"Noto Serif JP",serif;color:var(--gold-dark);font-size:14px;line-height:2.3}
.features-text .rule{margin-bottom:18px}

.points{display:flex;justify-content:center;gap:60px;height:370px;padding-top:10px}
.point{width:240px}
.point .ph{width:210px;height:210px;margin:0 auto;border-radius:50%;border:5px solid var(--cream)}
.point:nth-child(1) .ph{background:radial-gradient(circle at 45% 40%,#d8cbbb,#8c7a6a)}
.point:nth-child(2) .ph{background:radial-gradient(circle at 50% 50%,#f3d8d2,#d6a8a0)}
.point:nth-child(3) .ph{background:radial-gradient(circle at 50% 40%,#e6ddd0,#9c8b7a)}
.point h3{font-family:"Noto Serif JP",serif;font-size:14px;color:var(--gold);text-align:center;margin:12px 0 4px}
.point p{font-size:11px;line-height:1.9}

.flow{width:640px;margin:0 auto;height:200px;border:1px solid var(--gold-light);padding:20px 30px;text-align:center}
.flow h2{font-family:"Noto Serif JP",serif;font-size:18px;color:var(--gold-dark);letter-spacing:.08em;margin-bottom:14px}
.flow-steps{display:flex;justify-content:center;align-items:center;gap:8px}
.step{width:110px;height:110px;border-radius:50%;border:1px solid var(--gold);display:flex;align-items:center;justify-content:center;font-family:"Noto Serif JP",serif;font-size:19px;color:var(--gold-dark);background:var(--white)}
.step.small{font-size:15px}
.btn{display:block;margin:0 auto;width:280px;background:var(--gold);color:var(--white);text-align:center;font-family:"Noto Serif JP",serif;font-size:13px;padding:10px 0}
.btn.out{background:var(--white);color:var(--gold);border:1px solid var(--gold);width:200px;font-size:12px;padding:7px 0}
.about-link{margin-top:28px}

/* select style */
.select{height:620px;padding-top:80px}
.styles{display:flex;justify-content:center;gap:40px;margin-top:24px}
.style{width:360px;text-align:center}
.style .ph{height:230px}
.style:nth-child(1) .ph{background:linear-gradient(135deg,#ece6df,#b9aa98)}
.style:nth-child(2) .ph{background:linear-gradient(135deg,#d9cfc3,#7d6e62)}
.style h3{font-family:"Noto Serif JP",serif;font-size:15px;color:var(--gold);margin:16px 0 8px}
.style h3:before,.style h3:after{content:"—";color:var(--gold-light);margin:0 10px}
.style p{font-size:11.5px;line-height:2;height:120px;margin-bottom:10px}

/* faq */
.faq{height:590px;padding:60px 110px 0}
.faq-list{margin-top:20px}
.qa{border-bottom:1px solid var(--line);padding:9px 0}
.qa .q{display:flex;align-items:center;gap:12px;font-family:"Noto Serif JP",serif;font-size:13px}
.mark{width:22px;height:22px;border-radius:50%;background:var(--gold);color:var(--white);font-size:11px;display:flex;align-items:center;justify-content:center;flex:none;font-family:"Noto Serif JP",serif}
.mark.a{background:var(--white);border:1px solid var(--gold);color:var(--gold)}
.qa .a-text{display:flex;gap:12px;font-size:11px;margin-top:5px;line-height:1.8}

/* news */
.news{display:flex;gap:60px;height:220px;padding:20px 110px 0}
.news-col{flex:1}
.news-col h2{font-family:"Cormorant Garamond",serif;font-style:italic;color:var(--gold);font-size:24px;font-weight:500;border-bottom:1px solid var(--gold-light);line-height:1.5}
.news-col h2 small{font-family:"Noto Serif JP",serif;font-style:normal;font-size:11px;color:var(--muted);margin-left:8px}
.news-col li{list-style:none;font-size:11px;border-bottom:1px dotted var(--line);padding:4px 0;display:flex;gap:16px}
.news-col time{color:var(--gold);flex:none}

/* banners */
.banners{display:flex;height:180px}
.banner{flex:1;position:relative}
.banner .ph{height:100%}
.banner:nth-child(1) .ph{background:linear-gradient(135deg,#e9e2da,#b6a696)}
.banner:nth-child(2) .ph{background:linear-gradient(135deg,#eef1f4,#b8c2cc)}
.banner:nth-child(3) .ph{background:linear-gradient(135deg,#f0e6e2,#c8a9a0)}
.banner:nth-child(4) .ph{background:linear-gradient(135deg,#efe9df,#c6b59a)}
.banner span{position:absolute;right:16px;bottom:56px;background:rgba(255,255,255,.9);font-family:"Noto Serif JP",serif;font-size:14px;color:var(--gold-dark);padding:6px 18px}

/* counselor */
.counselor{height:380px;background:var(--cream);position:relative;padding:50px 0 0 140px}
.counselor .tag{display:inline-block;background:var(--gold);color:var(--white);font-family:"Noto Serif JP",serif;font-size:12px;padding:2px 14px}
.counselor .name{font-family:"Noto Serif JP",serif;font-size:18px;margin:10px 0 4px}
.counselor .name small{font-size:12px;color:var(--muted);margin-left:10px}
.counselor h2{font-family:"Noto Serif JP",serif;font-size:21px;color:var(--gold-dark);margin:8px 0}
.counselor p{width:600px;font-size:11.5px;line-height:2}
.counselor .ph{position:absolute;right:150px;top:70px;width:230px;height:230px;border-radius:50%;background:radial-gradient(circle at 50% 40%,#d9cabb,#7e6b5c)}

/* about */
.about{padding-top:60px;text-align:center}
.map{margin-top:24px;height:300px;background:linear-gradient(180deg,#ececea,#dcdcd8)}
.about-info{margin-top:24px;font-size:12px}
.about-info .tel{justify-content:center;font-size:24px;margin:4px 0}
.about-btns{display:flex;justify-content:center;gap:16px;margin-top:16px}
.about-btns .btn{margin:0;width:180px;font-size:12px;padding:7px 0}

/* footer */
.site-footer{position:absolute;top:4600px;left:0;width:1200px;height:272px}
.footer-band{height:14px;background:var(--gold)}
.footer-main{display:flex;justify-content:space-between;align-items:center;padding:24px 60px 0}
.footer-nav{display:flex;justify-content:space-between;align-items:center;font-size:11px;padding:18px 0;border-top:1px solid var(--line);margin:20px 60px 0}
.footer-links{display:flex;gap:20px}
.badge{width:190px;height:50px;border:1px solid var(--line);background:var(--cream)}
.copy{background:var(--gold);color:var(--white);text-align:center;font-size:10px;height:34px;line-height:34px;position:absolute;bottom:0;left:0;right:0}
</style>
</head>
<body>

<header class="site-header">
  <div class="header-top">
    <div class="brand">
      <span class="brand-name">SELUMIA</span>
      <span class="brand-sub">Marriage Agency SELUMIA<br>群馬の結婚相談所 セルミア</span>
    </div>
    <div class="contact">
      <div class="tel"><svg width="18" height="18" viewBox="0 0 24 24"><path fill="#9a7f45" d="M6.6 10.8a15 15 0 0 0 6.6 6.6l2.2-2.2c.3-.3.7-.4 1-.2 1.1.4 2.3.6 3.6.6.6 0 1 .4 1 1V20c0 .6-.4 1-1 1A17 17 0 0 1 3 4c0-.6.4-1 1-1h3.5c.6 0 1 .4 1 1 0 1.3.2 2.5.6 3.6.1.3 0 .7-.2 1z"/></svg>027-410-5828</div>
      <div class="tel-note">受付時間 10:00〜19:00（火曜定休）</div>
      <div class="header-btns"><a class="btn-s light">無料カウンセリング予約</a><a class="btn-s">資料請求・お問い合わせ</a></div>
    </div>
  </div>
  <nav class="gnav">
    <a>初めての方へ<small>First</small></a>
    <a>料金・サービス<small>Price</small></a>
    <a>ご成婚までの流れ<small>Flow</small></a>
    <a>会員データ<small>Data</small></a>
    <a>婚活パーティー<small>Party</small></a>
    <a>よくある質問<small>Q&amp;A</small></a>
  </nav>
</header>

<section class="hero">
  <div class="ph" role="img" aria-label="黒いスーツ姿の婚活カウンセラー8名が並ぶ集合写真"></div>
  <div class="hero-copy">
    <h1>わたし達だから知っている「成婚の法則」</h1><br>
    <p>多くの結婚式をプロデュースしてきた私たちがあなたの婚活を完全サポート</p>
  </div>
</section>
<div class="dots"><span></span><span></span><span></span><span></span></div>

<section class="features">
  <div class="ph" role="img" aria-label="窓辺に立つウエディングドレスの花嫁の写真"></div>
  <div class="features-text">
    <div class="rule">SELUMIAの特徴</div>
    <p>ブライダルの現場で多くの結婚式を手がけてきた私たちが運営する結婚相談所です。<br>
    お一人おひとりに専任のカウンセラーがつき、出会いからご成婚まで寄り添います。<br>
    「仲人型婚活」と「婚活パーティー」、あなたに合ったスタイルを選べます。<br>
    ご成婚後も結婚式や新生活の準備まで、安心してご相談いただけます。<br>
    わたし達だから知っている成婚の法則で、あなたの幸せを全力で応援します。<br>
    まずはお気軽に無料カウンセリングへお越しください。</p>
  </div>
</section>

<div class="points">
  <div class="point">
    <div class="ph" role="img" aria-label="カウンセラーと女性が面談する写真"></div>
    <h3>専任カウンセラーが伴走</h3>
    <p>入会から成婚まで同じカウンセラーが担当します。お相手選びやお見合いの準備、交際中の悩みまで丁寧に伺い、あなたらしい婚活を一緒に進めます。</p>
  </div>
  <div class="point">
    <div class="ph" role="img" aria-label="淡いピンクのバラのブーケの写真"></div>
    <h3>結婚式のプロが運営</h3>
    <p>数多くの結婚式を手がけてきた経験を生かし、ご成婚後の式や披露宴の準備までサポートします。会員様だけの特典もご用意しています。</p>
  </div>
  <div class="point">
    <div class="ph" role="img" aria-label="書類を前に相談する男女の写真"></div>
    <h3>選べる二つの婚活スタイル</h3>
    <p>じっくり向き合う仲人型婚活と、気軽に参加できる婚活パーティー。ライフスタイルに合わせて組み合わせることもできます。</p>
  </div>
</div>

<div class="flow">
  <h2>SELUMIAは成婚主義の結婚相談所です。</h2>
  <div class="flow-steps">
    <div class="step">出会い</div>
    <svg width="20" height="20" viewBox="0 0 20 20"><path d="M6 3l8 7-8 7" fill="none" stroke="#b59a5f" stroke-width="1.5"/></svg>
    <div class="step">交際</div>
    <svg width="20" height="20" viewBox="0 0 20 20"><path d="M6 3l8 7-8 7" fill="none" stroke="#b59a5f" stroke-width="1.5"/></svg>
    <div class="step small">プロポーズ</div>
    <svg width="20" height="20" viewBox="0 0 20 20"><path d="M6 3l8 7-8 7" fill="none" stroke="#b59a5f" stroke-width="1.5"/></svg>
    <div class="step">結婚</div>
  </div>
</div>
<div class="about-link"><a class="btn">SELUMIAについて</a></div>

<section class="select">
  <div class="sec-head"><span class="en">Select Style</span><span class="ja">選べる婚活スタイル</span></div>
  <div class="styles">
    <div class="style">
      <div class="ph" role="img" aria-label="ウエディングドレスの花嫁とタキシードの新郎の写真"></div>
      <h3>仲人型婚活スタイル</h3>
      <p>専任カウンセラーがあなたの希望を伺い、ぴったりのお相手をご紹介します。お見合いの日程調整や当日のアドバイス、交際中のフォローまで、仲人がしっかりとサポート。真剣に結婚を考える方に選ばれています。</p>
      <a class="btn out">詳しく見る</a>
    </div>
    <div class="style">
      <div class="ph" role="img" aria-label="婚活パーティーで笑顔で談笑する男女の写真"></div>
      <h3>婚活パーティースタイル</h3>
      <p>年齢や趣味などテーマ別のパーティーを定期的に開催しています。少人数制で一人ひとりとゆっくり話せるのが魅力。スタッフが会話のきっかけ作りもお手伝いするので、初めての方も安心です。</p>
      <a class="btn out">詳しく見る</a>
    </div>
  </div>
</section>

<section class="faq">
  <div class="sec-head"><span class="en">Q&amp;A</span><span class="ja">よくあるご質問</span></div>
  <div class="faq-list">
    <div class="qa"><div class="q"><span class="mark">Q</span>結婚相談所は初めてですが、どのように始めればよいですか？</div>
      <div class="a-text"><span class="mark a">A</span>まずは無料カウンセリングにお越しください。婚活の進め方やサービス内容をご説明し、ご希望を伺ったうえで最適なプランをご提案します。情報収集だけでもお気軽にどうぞ。</div></div>
    <div class="qa"><div class="q"><span class="mark">Q</span>入会に必要な書類はありますか？</div>
      <div class="a-text"><span class="mark a">A</span>本人確認書類、独身証明書、収入証明書、卒業証明書などをご用意いただきます。詳しくはカウンセリング時にご案内します。</div></div>
    <div class="qa"><div class="q"><span class="mark">Q</span>会員はどのような年代の方が多いですか？</div>
      <div class="a-text"><span class="mark a">A</span>女性は20代後半から30代、男性は30代から40代前半の方が中心です。地元で真剣に結婚を考える方が多く在籍しています。</div></div>
    <div class="qa"><div class="q"><span class="mark">Q</span>仕事が忙しくても活動できますか？</div>
      <div class="a-text"><span class="mark a">A</span>お見合いの日程調整はカウンセラーが代行します。平日夜や土日を中心に、ご都合に合わせて無理なく活動いただけます。</div></div>
    <div class="qa"><div class="q"><span class="mark">Q</span>パーティーだけの参加もできますか？</div>
      <div class="a-text"><span class="mark a">A</span>はい、会員登録なしでもご参加いただけるパーティーを多数開催しています。開催日程はパーティー情報ページをご覧ください。</div></div>
    <div class="qa"><div class="q"><span class="mark">Q</span>成婚後のサポートはありますか？</div>
      <div class="a-text"><span class="mark a">A</span>結婚式のご相談や会場のご紹介など、ブライダルの経験を生かした特典をご用意しています。</div></div>
  </div>
</section>

<section class="news">
  <div class="news-col">
    <h2>Information<small>お知らせ</small></h2>
    <ul>
      <li><time>2017.01.20</time>春の婚活パーティー日程を公開しました</li>
      <li><time>2017.01.15</time>無料カウンセリングの予約枠を拡大しました</li>
      <li><time>2017.01.10</time>年始の営業時間についてのお知らせ</li>
      <li><time>2017.01.05</time>会員様限定ブライダル特典のご案内</li>
      <li><time>2016.12.25</time>ホームページをリニューアルしました</li>
    </ul>
  </div>
  <div class="news-col">
    <h2>Blog<small>ブログ</small></h2>
    <ul>
      <li><time>2017.01.19</time>お見合いで好印象を与える服装のコツ</li>
      <li><time>2017.01.14</time>成婚されたお二人からのメッセージ</li>
      <li><time>2017.01.09</time>初デートのお店選びで大切なこと</li>
      <li><time>2017.01.04</time>新年に始める婚活のすすめ</li>
      <li><time>2016.12.28</time>カウンセラーが語る成婚の法則</li>
    </ul>
  </div>
</section>

<div class="banners">
  <div class="banner"><div class="ph" role="img" aria-label="手を重ねるカップルの写真"></div><span>初めての方へ</span></div>
  <div class="banner"><div class="ph" role="img" aria-label="グラフと資料の写真"></div><span>会員数・実績データ</span></div>
  <div class="banner"><div class="ph" role="img" aria-label="指輪を交換する新郎新婦の写真"></div><span>ご成婚までの流れ</span></div>
  <div class="banner"><div class="ph" role="img" aria-label="婚活パーティー会場の写真"></div><span>婚活パーティー</span></div>
</div>

<section class="counselor">
  <span class="tag">婚活カウンセラー</span>
  <div class="name">代表　水野 彩花<small>ブライダルプランナー歴15年</small></div>
  <h2>前職はブライダル業界。</h2>
  <p>これまで数多くの結婚式に携わり、たくさんのご夫婦の門出を見届けてきました。その経験から感じるのは、幸せな結婚には出会いの質と、二人で歩む準備が大切だということです。婚活は不安や迷いがつきものですが、一人で抱え込む必要はありません。お一人おひとりのペースに寄り添い、あなたらしい幸せの形を一緒に見つけていきたいと思っています。まずはお気軽にお話を聞かせてください。</p>
  <div class="ph" role="img" aria-label="笑顔の女性カウンセラーの写真"></div>
</section>

<section class="about">
  <div class="sec-head"><span class="en">About us</span><span class="ja">アクセス・店舗情報</span></div>
  <div class="map" role="img" aria-label="店舗周辺の地図"></div>
  <div class="about-info">
    <p>SELUMIA　群馬県緑野市中央町2-14 セルミアビル3F</p>
    <div class="tel"><svg width="20" height="20" viewBox="0 0 24 24"><path fill="#9a7f45" d="M6.6 10.8a15 15 0 0 0 6.6 6.6l2.2-2.2c.3-.3.7-.4 1-.2 1.1.4 2.3.6 3.6.6.6 0 1 .4 1 1V20c0 .6-.4 1-1 1A17 17 0 0 1 3 4c0-.6.4-1 1-1h3.5c.6 0 1 .4 1 1 0 1.3.2 2.5.6 3.6.1.3 0 .7-.2 1z"/></svg>027-410-5828</div>
    <p>営業時間 10:00〜19:00（火曜定休）</p>
    <div class="about-btns"><a class="btn">無料カウンセリング</a><a class="btn">資料請求</a></div>
  </div>
</section>

<footer class="site-footer">
  <div class="footer-band"></div>
  <div class="footer-main">
    <div class="brand"><span class="brand-name">SELUMIA</span><span class="brand-sub">群馬の結婚相談所 セルミア<br>群馬県緑野市中央町2-14</span></div>
    <div class="contact">
      <div class="tel"><svg width="18" height="18" viewBox="0 0 24 24"><path fill="#9a7f45" d="M6.6 10.8a15 15 0 0 0 6.6 6.6l2.2-2.2c.3-.3.7-.4 1-.2 1.1.4 2.3.6 3.6.6.6 0 1 .4 1 1V20c0 .6-.4 1-1 1A17 17 0 0 1 3 4c0-.6.4-1 1-1h3.5c.6 0 1 .4 1 1 0 1.3.2 2.5.6 3.6.1.3 0 .7-.2 1z"/></svg>027-410-5828</div>
      <div class="header-btns"><a class="btn-s light">無料カウンセリング予約</a><a class="btn-s">資料請求・お問い合わせ</a></div>
    </div>
  </div>
  <div class="footer-nav">
    <div class="footer-links"><a>HOME</a><a>初めての方へ</a><a>料金・サービス</a><a>ご成婚までの流れ</a><a>会員データ</a><a>婚活パーティー</a><a>会社概要</a></div>
    <div class="badge" role="img" aria-label="加盟団体のバッジ"></div>
  </div>
  <div class="copy">Copyright © SELUMIA All Rights Reserved.</div>
</footer>

</body>
</html>
```